Healthtech Wearable Device Product Packaging Design

We need a new product packaging design for SEA market with an international look to it.
Attached is our current China/Taiwan for your reference.
Our company name: Velmorix means guiding light and provide care on 3 levels: Government community care, corporate health management, and family care.
Our company color schem is orange and white.

Target Market(s)

Health tech, Southeast Asia, International look
The final design should communicate "bringing healthcare closer you", a touch of friendliness, love and tender care. It does not give off just another wearable watch vibe.

Requirements
Must have
• Color scheme: Orange and white
Simple yet professional looking
Health tech but think out of the box
Distribution to B2B channel
Nice to have
• Eye catchy, trendy, support sustainability in one way or another
Should not have
• overcrowding feel, boring

```html
<!DOCTYPE html>
<html lang="en">
<head>
<meta charset="utf-8">
<title>Velmorix VX 520 Packaging</title>
<link rel="stylesheet" href="https://fonts.googleapis.com/css2?family=Comfortaa:wght@300&family=Open+Sans:ital,wght@0,400;0,800;1,400&display=swap">
<style>
  :root {
    --canvas: #e4e4e4;
    --white: #ffffff;
    --paper: #f7f7f7;
    --ink: #3b3534;
    --orange: #efb12a;
    --orange-deep: #e0921a;
    --orange-side: #d98a1a;
    --orange-text: #eeaa22;
    --band-text: #fff7e8;
    --badge-blue: #3d7fcf;
    --badge-grey: #cfcfcf;
    --device-dark: #4a4a4c;
    --device-mid: #6c6c6e;
  }
  * { margin: 0; padding: 0; box-sizing: border-box; }
  html, body { width: 1200px; height: 1200px; overflow: hidden; background: var(--canvas); }
  .canvas { position: relative; width: 1200px; height: 1200px; }

  .box-front {
    position: absolute; left: 230px; top: 60px; width: 740px; height: 860px;
    background: linear-gradient(160deg, var(--white) 0%, var(--paper) 100%);
    overflow: hidden;
    box-shadow: 0 18px 40px rgba(0,0,0,0.12);
  }
  .fitness-pattern {
    position: absolute; inset: 0;
    background: radial-gradient(ellipse at 30% 35%, rgba(200,200,200,0.18), transparent 60%),
                radial-gradient(ellipse at 80% 65%, rgba(200,200,200,0.16), transparent 55%);
  }
  .wave-ornament {
    position: absolute; left: 0; top: 300px; width: 740px; height: 300px;
    background: radial-gradient(ellipse at 70% 40%, rgba(243,190,120,0.28), transparent 65%),
                radial-gradient(ellipse at 25% 70%, rgba(243,200,140,0.22), transparent 60%);
  }
  .brand-name {
    position: absolute; left: 0; right: 0; top: 90px; text-align: center;
    font-family: 'Comfortaa', sans-serif; font-weight: 300; font-size: 92px;
    color: var(--ink); letter-spacing: 2px;
  }
  .device-photo {
    position: absolute; left: 215px; top: 230px; width: 330px; height: 330px;
    border-radius: 46% 54% 50% 50%;
    background: radial-gradient(circle at 50% 50%, transparent 44%, var(--device-mid) 45%, var(--device-dark) 70%, transparent 71%);
  }
  .tagline {
    position: absolute; left: 60px; top: 560px;
    font-family: 'Open Sans', sans-serif; font-weight: 800; font-size: 46px; line-height: 1.12;
    color: var(--orange-text);
  }
  .tagline .line-two { display: block; padding-left: 26px; }
  .band {
    position: absolute; left: 0; right: 0; bottom: 0; height: 180px;
    background: linear-gradient(180deg, var(--orange) 0%, var(--orange-deep) 100%);
  }
  .band-info {
    position: absolute; left: 0; right: 40px; top: 26px;
    display: flex; justify-content: flex-end; align-items: center; gap: 12px;
  }
  .compliance {
    font-family: 'Open Sans', sans-serif; font-size: 15px; color: var(--band-text);
  }
  .divider { width: 1px; height: 22px; background: var(--band-text); }
  .badge-round { width: 26px; height: 22px; border-radius: 50%; background: var(--badge-grey); }
  .badge-rect { width: 48px; height: 22px; border-radius: 3px; background: var(--badge-blue); }
  .badge-small { width: 22px; height: 18px; border-radius: 3px; background: var(--white); }

  .box-side {
    position: absolute; left: 230px; top: 920px; width: 740px; height: 170px;
    background: linear-gradient(180deg, var(--orange-side) 0%, #c97914 100%);
    display: flex; align-items: center; justify-content: center;
  }
  .model-name {
    font-family: 'Open Sans', sans-serif; font-style: italic; font-weight: 400; font-size: 64px;
    color: #e9e4dc; letter-spacing: 4px;
  }
</style>
</head>
<body>
<div class="canvas">
  <section class="box-front">
    <div class="fitness-pattern" role="img" aria-label="Faint pattern of fitness and health icons: kettlebell, stopwatch, dumbbell, heart with pulse line"></div>
    <div class="wave-ornament" role="img" aria-label="Soft flowing orange line waves across the panel"></div>
    <div class="brand-name">Velmorix</div>
    <div class="device-photo" role="img" aria-label="Product photo of a grey fitness band whose screen shows an SpO2 reading of 98"></div>
    <h1 class="tagline">Bringing<span class="line-two">Healthcare Closer to You</span></h1>
    <div class="band">
      <div class="band-info">
        <span class="compliance">Complies with ORTA Standards RA204417</span>
        <span class="divider"></span>
        <span class="badge-round"></span>
        <span class="badge-rect"></span>
        <span class="badge-small"></span>
      </div>
    </div>
  </section>
  <section class="box-side">
    <span class="model-name">VX 520</span>
  </section>
</div>
</body>
</html>
```